PPT template for boutique strategic planning, accounting and taxation firm

We are a boutique firm that provides strategic, accounting and tax advice to our clients. The work we are doing is increasingly strategic work and we are required to produce reports and presentations and our current templates are simply not sufficient.
As you can see from the examples attached, we have very limited skills in house re design! We have attached a PPT document and word document (that should be PPT) that we use regularly as examples of the content. Excel worksheets are regularly embedded into the presentation (in both blue and orange - see below re colours)
Not specific to one area but typically these clients are famous for their own brand and are creating value in their industry through creating their own brand and we want to produce documents of a similar standard.
A Powerpoint Document Slide Template
Cover page layout, back page, intermediate page heading, in colours and styles based on the logo, title styles, and an intermediate or chapter heading slide style. Many of our presentations contain slides with tables, diagrams, flowcharts and text, including simple lists of bullet points. As above, you will see in our style guide that we have three coloured logos – we would like one version in blue and one version in orange please. Again, the cover should be bold and draw attention but remain professional.
We are looking for something that works in both 4:3 and 16:9 (or two templates please)
We like a clear professional and simple look.
Deliverable: PowerPoint template file (.potx extension) for PowerPoint 2007 with at least a “cover” layout, a “title and content” layout, and a simplified slide layout, as well as “back cover”. Please embed any fonts used.
Target Market(s)
Many of our clients are retail clients or have strong brands of their own.
Industry/Entity Type
Accounting
Requirements
Must have
- Harrowby & Co logo on each page.
Must have a cover page (please be bold but professional)
A selection of "standard" slides - dot points, detailed written content, example diagrams, flow charts etc.
A back cover
Nice to have
- We would like to have a copy done in both the blue and orange versions attached. Happy for the winner to complete the other colour after the winner is selected.
Prefer Arial logo but open to suggestions. Must be easy to read and professional
Should not have
- Nothing cartoonish

```html
<!DOCTYPE html>
<html lang="en">
<head>
<meta charset="utf-8">
<title>Harrowby &amp; Co — Presentation Template</title>
<link href="https://fonts.googleapis.com/css2?family=Mulish:ital,wght@0,400;0,600;0,700;0,800;1,400&display=swap" rel="stylesheet">
<style>
  :root{
    --board:#474d55;
    --teal:#25a9a9;
    --teal-dark:#1a8b8e;
    --teal-light:#3cc3c0;
    --teal-ink:#1c7f82;
    --ink:#2c3a42;
    --grey-text:#5b6166;
    --blue:#1a7cc4;
    --blue-side:#135f9d;
    --blue-band:#1b62b0;
    --blue-band-light:#2b86cf;
    --navy:#1b3550;
    --orange:#f4a124;
    --orange-side:#d2841a;
    --cyan:#1fb3b3;
    --cyan-side:#168a8f;
    --panel-1:#ececec;
    --panel-2:#dcdcdc;
    --panel-3:#c2c2c2;
    --white:#ffffff;
  }
  *{margin:0;padding:0;box-sizing:border-box}
  html,body{width:1031px;height:1200px;overflow:hidden;background:var(--board)}
  body{font-family:"Mulish",Arial,sans-serif}
  .board{position:absolute;left:0;top:0;width:900px;height:1048px;transform:scale(1.1456);transform-origin:0 0}
  .slide{position:absolute;width:417px;height:321px;background:var(--white);overflow:hidden}
  .slide--teal{background:var(--teal)}
  .s-cover{left:25px;top:28px}
  .s-section{left:453px;top:28px}
  .s-pie{left:25px;top:357px}
  .s-text{left:453px;top:357px}
  .s-bars{left:18px;top:693px;width:418px}
  .s-back{left:453px;top:693px}
  .abs{position:absolute}

  /* firm name */
  .firm-name{position:absolute;font-weight:700;color:var(--ink);white-space:nowrap}

  /* footer band */
  .footer{position:absolute;left:0;bottom:0;width:100%;height:43px;background:var(--teal)}
  .footer svg{position:absolute;left:0;top:0}
  .footer__title{position:absolute;left:62px;top:13px;color:var(--white);font-size:8.5px;font-weight:600}
  .footer__sub{position:absolute;left:62px;top:24px;color:var(--white);font-size:4.6px}
  .footer__by{position:absolute;left:170px;top:15px;color:var(--teal-ink);font-size:5.6px;font-weight:800;letter-spacing:.3px}
  .footer__role{position:absolute;left:170px;top:23px;color:var(--teal-ink);font-size:6px;font-weight:700}
  .footer .firm-name{right:22px;top:14px;font-size:12px}

  /* section slide */
  .section-num{position:absolute;left:63px;top:90px;width:90px;height:90px;border-radius:50%;overflow:hidden;background:var(--teal)}
  .section-num span{position:absolute;left:0;top:0;width:100%;line-height:90px;text-align:center;color:var(--white);font-size:42px;font-weight:800;letter-spacing:-1px}
  .section-title{position:absolute;left:183px;top:93px;font-size:32px;font-weight:700;color:#3d4448;letter-spacing:-.5px}
  .section-list{position:absolute;left:184px;top:132px;font-size:12.5px;line-height:16px;color:#4d5256}

  .note{position:absolute;font-size:7px;line-height:9px;color:#555b60}

  /* text slide */
  .doc{position:absolute;left:34px;top:20px;width:350px}
  .doc__title{font-size:14px;font-weight:700;color:#3a4045}
  .doc__subtitle{font-size:10px;color:var(--teal);margin-bottom:8px}
  .doc p{font-size:6.2px;line-height:8.7px;color:var(--grey-text);margin-bottom:7px}
  .doc__quote{border-top:1px solid #a9dcdc;border-bottom:1px solid #a9dcdc;padding:6px 0;margin:6px 0 9px}
  .doc__quote p{font-style:italic;color:var(--teal);margin:0}

  /* list panel */
  .panel{position:absolute;left:259px;top:37px;width:131px}
  .panel__head{height:27px;background:var(--teal);color:var(--white);font-size:12px;font-weight:800;text-align:center;line-height:27px}
  .panel__item{position:relative;height:65px;padding:10px 8px 0 23px;font-size:6.6px;line-height:8.6px;color:#4c5155}
  .panel__item:nth-child(2){background:var(--panel-1)}
  .panel__item:nth-child(3){background:var(--panel-2)}
  .panel__item:nth-child(4){background:var(--panel-3)}
  .panel__bullet{position:absolute;left:-9px;top:23px;width:18px;height:18px;border-radius:50%}

  /* back cover */
  .url-band{position:absolute;left:0;top:216px;width:100%;height:43px;background:var(--blue-band)}
  .url-band svg{position:absolute;left:0;top:0}
  .url-band__text{position:absolute;left:0;top:0;width:100%;line-height:43px;text-align:center;color:var(--white);font-size:15px;font-weight:800}
</style>
</head>
<body>
<div class="board">

  <!-- Cover -->
  <section class="slide slide--teal s-cover">
    <div class="firm-name" style="left:0;width:100%;text-align:center;top:143px;font-size:25px">Harrowby &amp; Co</div>
  </section>

  <!-- Section heading -->
  <section class="slide s-section">
    <div class="section-num">
      <svg class="abs" width="90" height="90" viewBox="0 0 90 90"><polygon points="70,28 160,118 100,160 22,70" fill="var(--teal-dark)"/></svg>
      <span>01</span>
    </div>
    <div class="section-title">Overview</div>
    <div class="section-list">The company<br>Meet the team</div>
    <footer class="footer">
      <svg width="70" height="43" viewBox="0 0 70 43"><polygon points="0,0 46,0 0,43" fill="var(--teal-dark)"/><polygon points="0,12 30,43 0,43" fill="var(--teal-light)"/></svg>
      <div class="footer__title">Presentation name</div>
      <div class="footer__sub">Other text to be included here</div>
      <div class="footer__by">BY: PETER HALE</div>
      <div class="footer__role">Executive manager</div>
      <div class="firm-name">Harrowby &amp; Co</div>
    </footer>
  </section>

  <!-- Pie chart -->
  <section class="slide s-pie">
    <svg class="abs" width="417" height="280" viewBox="0 0 417 280" role="img" aria-label="Pie chart with three segments">
      <path d="M327,132 A117,51 0 0 1 109,157.5 L109,197.5 A117,51 0 0 0 327,172 Z" fill="var(--blue-side)"/>
      <path d="M109,157.5 A117,51 0 0 1 93,132 L93,172 A117,51 0 0 0 109,197.5 Z" fill="var(--cyan-side)"/>
      <path d="M210,132 L210,81 A117,51 0 1 1 109,157.5 Z" fill="var(--blue)"/>
      <path d="M210,132 L109,157.5 A117,51 0 0 1 151.5,88 Z" fill="var(--cyan)"/>
      <path d="M210,132 L151.5,88 A117,51 0 0 1 210,81 Z" fill="var(--orange)"/>
      <g fill="none" stroke-width=".8">
        <polyline points="106,46 185,46 185,100" stroke="var(--orange)"/>
        <polyline points="302,58 266,58 266,140" stroke="var(--navy)"/>
        <polyline points="55,211 55,135 147,135" stroke="var(--cyan)"/>
      </g>
      <circle cx="106" cy="46" r="4" fill="var(--orange)"/>
      <circle cx="185" cy="100" r="4" fill="#f7b24a"/>
      <circle cx="302" cy="58" r="4" fill="var(--navy)"/>
      <circle cx="266" cy="140" r="4" fill="var(--navy)"/>
      <circle cx="55" cy="211" r="4" fill="var(--cyan)"/>
      <circle cx="147" cy="135" r="4" fill="#45c1bf"/>
    </svg>
    <div class="note" style="left:21px;top:33px;width:80px">Lorem ipsum dolor sit amet, consectetur adipiscing elit.</div>
    <div class="note" style="left:311px;top:44px;width:100px">Lorem ipsum dolor sit amet, consectetur adipiscing elit. Nullam a orci sit amet magna varius porttitor eu quis nisi.</div>
    <div class="note" style="left:28px;top:225px;width:100px">Lorem ipsum dolor sit amet, consectetur adipiscing elit. Nullam a orci sit amet magna varius porttitor eu quis nisi.</div>
    <footer class="footer">
      <svg width="70" height="43" viewBox="0 0 70 43"><polygon points="0,0 46,0 0,43" fill="var(--teal-dark)"/><polygon points="0,12 30,43 0,43" fill="var(--teal-light)"/></svg>
      <div class="footer__title">Presentation name</div>
      <div class="footer__sub">Other text to be included here</div>
      <div class="footer__by">BY: PETER HALE</div>
      <div class="footer__role">Executive manager</div>
      <div class="firm-name">Harrowby &amp; Co</div>
    </footer>
  </section>

  <!-- Text content -->
  <section class="slide s-text">
    <div class="doc">
      <div class="doc__title">Lorem ipsum.</div>
      <div class="doc__subtitle">Subtitle</div>
      <p>Lorem ipsum dolor sit amet, consectetur adipiscing elit. Nullam a orci sit amet magna varius porttitor eu quis nisi. Ut viverra mi a leo lacinia molestie non sed quam. Pellentesque habitant morbi tristique senectus et netus et malesuada fames ac turpis egestas. Suspendisse tempor erat lorem, ac blandit libero porttitor vitae. Suspendisse faucibus nisi sed libero tristique, non luctus nulla viverra. Aenean porta quam sed accumsan imperdiet. Maecenas convallis auctor consectetur. Praesent posuere ullamcorper lectus sit amet viverra.</p>
      <p>Donec egestas nec leo in fringilla. Morbi sem metus, consequat non malesuada in, dictum nec elit. Phasellus quam eros, euismod ac enim vel, auctor dignissim ligula. Integer tempor tellus purus, ac cursus nisl sagittis pellentesque. Nullam luctus fermentum rhoncus.</p>
      <div class="doc__quote"><p>Quisque commodo felis vitae aliquam bibendum. Curabitur sapien velit, egestas eget eros vitae, fermentum pellentesque sapien.</p></div>
      <p>Aliquam vitae turpis massa. Nulla pharetra massa lorem, eget egestas diam vehicula a. Mauris sed justo urna. Curabitur facilisis nibh eget sollicitudin varius. Pellentesque semper eros eu quam elementum egestas. Integer vitae elit tellus. Fusce vitae lacus porta, venenatis justo quis, auctor sapien. Morbi pretium sapien vel nibh bibendum cursus. Nullam ullamcorper urna vitae lacus posuere pretium. Fusce eget arcu viverra, vehicula orci vel, vulputate lorem. Fusce sollicitudin accumsan tortor nec tincidunt.</p>
    </div>
    <footer class="footer">
      <svg width="70" height="43" viewBox="0 0 70 43"><polygon points="0,0 46,0 0,43" fill="var(--teal-dark)"/><polygon points="0,12 30,43 0,43" fill="var(--teal-light)"/></svg>
      <div class="footer__title">Presentation name</div>
      <div class="footer__sub">Other text to be included here</div>
      <div class="footer__by">BY: PETER HALE</div>
      <div class="footer__role">Executive manager</div>
      <div class="firm-name">Harrowby &amp; Co</div>
    </footer>
  </section>

  <!-- Bar chart with list -->
  <section class="slide s-bars">
    <svg class="abs" width="250" height="240" viewBox="0 0 250 240" role="img" aria-label="Bar chart in teal, orange and blue">
      <polygon points="48,168 128,146 224,160 142,198" fill="var(--teal)"/>
      <g>
        <rect x="96" y="128" width="11" height="30" fill="var(--blue)"/><rect x="107" y="128" width="4" height="30" fill="var(--blue-side)"/>
        <rect x="160" y="122" width="11" height="40" fill="var(--blue)"/><rect x="171" y="122" width="4" height="40" fill="var(--blue-side)"/>
        <rect x="196" y="100" width="11" height="60" fill="var(--blue)"/><rect x="207" y="100" width="4" height="60" fill="var(--blue-side)"/>
        <rect x="114" y="110" width="11" height="46" fill="var(--orange)"/><rect x="125" y="110" width="4" height="46" fill="var(--orange-side)"/>
        <rect x="84" y="128" width="11" height="40" fill="var(--orange)"/><rect x="95" y="128" width="4" height="40" fill="var(--orange-side)"/>
        <rect x="154" y="144" width="11" height="22" fill="var(--orange)"/><rect x="165" y="144" width="4" height="22" fill="var(--orange-side)"/>
        <rect x="193" y="132" width="11" height="40" fill="var(--orange)"/><rect x="204" y="132" width="4" height="40" fill="var(--orange-side)"/>
        <rect x="62" y="118" width="12" height="58" fill="var(--cyan)"/><rect x="74" y="118" width="4" height="58" fill="var(--cyan-side)"/>
        <rect x="98" y="144" width="12" height="36" fill="var(--cyan)"/><rect x="110" y="144" width="4" height="36" fill="var(--cyan-side)"/>
        <rect x="134" y="134" width="12" height="50" fill="var(--cyan)"/><rect x="146" y="134" width="4" height="50" fill="var(--cyan-side)"/>
        <rect x="174" y="122" width="12" height="68" fill="var(--cyan)"/><rect x="186" y="122" width="4" height="68" fill="var(--cyan-side)"/>
      </g>
    </svg>
    <div class="panel">
      <div class="panel__head">Lorem ipsum.</div>
      <div class="panel__item"><span class="panel__bullet" style="background:var(--orange)"></span>Lorem ipsum dolor sit amet, consectetur adipiscing elit. Nullam a orci sit amet magna varius porttitor eu quis nisi.</div>
      <div class="panel__item"><span class="panel__bullet" style="background:var(--cyan)"></span>Lorem ipsum dolor sit amet, consectetur adipiscing elit. Nullam a orci sit amet magna varius porttitor eu quis nisi.</div>
      <div class="panel__item"><span class="panel__bullet" style="background:var(--blue)"></span>Lorem ipsum dolor sit amet, consectetur adipiscing elit. Nullam a orci sit amet magna varius porttitor eu quis nisi.</div>
    </div>
    <footer class="footer" style="height:45px">
      <svg width="70" height="45" viewBox="0 0 70 45"><polygon points="0,0 46,0 0,45" fill="var(--teal-dark)"/><polygon points="0,12 30,45 0,45" fill="var(--teal-light)"/></svg>
      <div class="footer__title">Presentation name</div>
      <div class="footer__sub">Other text to be included here</div>
      <div class="footer__by">BY: PETER HALE</div>
      <div class="footer__role">Executive manager</div>
      <div class="firm-name" style="top:15px">Harrowby &amp; Co</div>
    </footer>
  </section>

  <!-- Back cover -->
  <section class="slide slide--teal s-back">
    <div class="firm-name" style="left:0;width:100%;text-align:center;top:143px;font-size:26px">Harrowby &amp; Co</div>
    <div class="url-band">
      <svg width="80" height="43" viewBox="0 0 80 43"><polygon points="0,0 60,0 0,43" fill="var(--blue-band-light)"/></svg>
      <div class="url-band__text">www.harrowbyco-advisors.com</div>
    </div>
  </section>

</div>
</body>
</html>
```